Logo & Visitenkarte für Speisewinkel
Zielgruppe
Die Jausenstation mit Hausmannskost
Aufgabenstellung
Telefonnummer 0471 596137
E-Mail speisewinkel@postfach-beispiel.at
Und den Firmennamen

```html
<!DOCTYPE html>
<html lang="de">
<head>
<meta charset="utf-8">
<title>Speisewinkel – Visitenkarte</title>
<link href="https://fonts.googleapis.com/css2?family=Oswald:wght@300;400&display=swap" rel="stylesheet">
<style>
  :root {
    --backdrop: #cbd0d3;
    --card: #ffffff;
    --ink: #1a1a1a;
    --accent: #b0bd1e;
  }
  html, body {
    margin: 0;
    width: 1200px;
    height: 1199px;
    overflow: hidden;
    background: var(--backdrop);
    font-family: "Oswald", sans-serif;
  }
  .card {
    position: absolute;
    left: 250px;
    width: 700px;
    height: 400px;
    background: var(--card);
  }
  .card--front { top: 147px; }
  .card--back { top: 652px; }

  .wordmark {
    position: absolute;
    inset: 0;
    display: flex;
    align-items: center;
    justify-content: center;
  }
  .wordmark__name {
    font-weight: 400;
    font-size: 70px;
    line-height: 1;
    color: var(--accent);
  }

  .back__name {
    position: absolute;
    left: 54px; top: 58px;
    margin: 0;
    font-weight: 400;
    font-size: 38px;
    line-height: 1;
    color: var(--accent);
  }
  .back__tagline {
    position: absolute;
    left: 54px; top: 127px;
    margin: 0;
    font-weight: 300;
    font-size: 21px;
    line-height: 1;
    color: var(--ink);
    letter-spacing: 0.2px;
  }
  .back__rule {
    position: absolute;
    left: 54px; top: 175px;
    width: 429px; height: 2px;
    background: var(--accent);
  }
  .contact {
    position: absolute;
    left: 54px;
    display: flex;
    align-items: flex-start;
    gap: 16px;
    font-weight: 300;
    font-size: 17px;
    line-height: 23px;
    color: var(--ink);
    text-transform: uppercase;
  }
  .contact svg { flex: none; width: 22px; height: 26px; fill: var(--ink); }
  .contact p { margin: 0; }
  .contact--phone { top: 199px; }
  .contact--address { top: 242px; }
  .contact--mail { top: 334px; gap: 10px; }
  .contact--phone p { padding-top: 6px; }
  .contact--address p { padding-top: 10px; }
  .contact--mail p { padding-top: 2px; }
  .contact--mail svg { width: 26px; height: 20px; }
</style>
</head>
<body>
  <section class="card card--front">
    <div class="wordmark">
      <span class="wordmark__name">Speisewinkel</span>
    </div>
  </section>

  <section class="card card--back">
    <h1 class="back__name">Speisewinkel</h1>
    <p class="back__tagline">DIE JAUSENSTATION MIT HAUSMANNSKOST</p>
    <div class="back__rule"></div>

    <div class="contact contact--phone">
      <svg viewBox="0 0 24 24" aria-hidden="true"><path d="M6.6 2.2c.6-.3 1.3-.1 1.7.5l2.1 3.5c.4.6.2 1.3-.3 1.7L8.6 9c1.1 2.6 3.1 4.8 5.6 6.2l1.2-1.5c.4-.5 1.1-.7 1.700-.4l3.6 1.9c.6.3.9 1 .6 1.7l-.9 2.4c-.4 1-1.4 1.6-2.5 1.4C9.9 19.5 4.3 13.6 3.3 5.8c-.1-1 .4-2 1.3-2.5z"/></svg>
      <p>0471 596137</p>
    </div>

    <div class="contact contact--address">
      <svg viewBox="0 0 24 28" aria-hidden="true"><path d="M12 1C6.5 1 2.5 5 2.5 10.2 2.5 17 12 27 12 27s9.5-10 9.5-16.8C21.5 5 17.5 1 12 1zm0 13.5a4.3 4.3 0 1 1 0-8.6 4.3 4.3 0 0 1 0 8.6z"/></svg>
      <p>Lindenweg 14<br>9020 Klagenfurt am Wörthersee<br>Österreich</p>
    </div>

    <div class="contact contact--mail">
      <svg viewBox="0 0 26 20" aria-hidden="true"><path d="M2 1h22c.8 0 1.5.7 1.5 1.5v1.2L13 11 .5 3.7V2.5C.5 1.7 1.2 1 2 1zM.5 6l12.5 7.3L25.5 6v11.5c0 .8-.7 1.5-1.5 1.5H2c-.8 0-1.5-.7-1.5-1.5z"/></svg>
      <p>speisewinkel@postfach-beispiel.at</p>
    </div>
  </section>
</body>
</html>
```